Brisk Nova residential and commercial cleaning

We need a Business card design for a new residential and commercial cleaning company based in UAE- Abu Dhabi named (BRISK NOVA)
we provide a residential cleaning service based in hourly rate (Maid Rent - Baby Setting), Also a commercial and offices cleaning.
Our logo is attached for your reference

Target Market(s)

Women who are 22 to 60 years old.

Industry/Entity Type

Residential

Requirements
Should not have
• it should not have an old-style fonts

```html
<!DOCTYPE html>
<html lang="en">
<head>
<meta charset="utf-8">
<title>Brisk Nova Business Card</title>
<link href="https://fonts.googleapis.com/css2?family=Open+Sans:wght@400;600;700&display=swap" rel="stylesheet">
<style>
  :root {
    --page-bg: #e9e7e3;
    --card-bg: #ffffff;
    --ink: #1f1f1f;
    --ink-soft: #333333;
    --brand-blue: #2f8fd3;
    --band-blue: #2a82bf;
    --band-edge: #1d6a9f;
    --leaf-green: #8cc63f;
  }
  * { box-sizing: border-box; margin: 0; padding: 0; }
  html, body {
    width: 1200px; height: 1023px; overflow: hidden;
    background: var(--page-bg);
    font-family: "Open Sans", Arial, sans-serif;
    color: var(--ink);
  }
  .canvas { position: relative; width: 1200px; height: 1023px; }
  .card {
    position: absolute; left: 150px; top: 254px;
    width: 900px; height: 515px;
    background: var(--card-bg);
    box-shadow: 0 14px 30px rgba(0,0,0,0.18);
    overflow: hidden;
  }
  .identity { position: absolute; left: 56px; top: 58px; width: 430px; }
  .brand { display: flex; align-items: center; gap: 14px; }
  .brand-mark {
    width: 46px; height: 46px; border-radius: 50%;
    background: var(--leaf-green);
  }
  .brand-name {
    font-size: 52px; font-weight: 700; color: var(--brand-blue);
    letter-spacing: -0.5px; line-height: 1;
  }
  .availability {
    margin-top: 44px; font-size: 21px; font-weight: 700; color: var(--ink);
  }
  .contacts { list-style: none; margin-top: 18px; }
  .contacts li {
    display: flex; align-items: center; gap: 12px;
    font-size: 19px; color: var(--ink-soft); line-height: 34px;
  }
  .contacts svg { width: 16px; height: 16px; flex: none; fill: var(--leaf-green); }
  .services { position: absolute; left: 530px; top: 58px; }
  .services-title { font-size: 21px; font-weight: 700; color: var(--ink); }
  .services-list { list-style: none; margin-top: 12px; padding-left: 36px; }
  .services-list li { font-size: 19px; color: var(--ink-soft); line-height: 38px; }
  .tagline-band {
    position: absolute; left: 0; bottom: 0; width: 100%; height: 58px;
    background: var(--band-blue);
    border-bottom: 8px solid var(--band-edge);
    display: flex; align-items: center; justify-content: space-between;
    padding: 0 26px;
  }
  .band-dot { width: 10px; height: 10px; border-radius: 50%; background: #ffffff; }
  .tagline {
    color: #ffffff; font-size: 20px; font-weight: 400; letter-spacing: 4px;
  }
</style>
</head>
<body>
<div class="canvas">
  <section class="card">
    <div class="identity">
      <div class="brand">
        <span class="brand-name">Brisk Nova</span>
        <span class="brand-mark"></span>
      </div>
      <p class="availability">Same Day Appointment Available !</p>
      <ul class="contacts">
        <li><svg viewBox="0 0 16 16"><circle cx="8" cy="4.5" r="3.5"/><path d="M1 16c0-4 3-6.5 7-6.5s7 2.5 7 6.5z"/></svg>Dana Harlow</li>
        <li><svg viewBox="0 0 16 16"><path d="M4 0h8a1.5 1.5 0 0 1 1.5 1.5v13A1.5 1.5 0 0 1 12 16H4a1.5 1.5 0 0 1-1.5-1.5v-13A1.5 1.5 0 0 1 4 0zm0 2v10h8V2z"/></svg>Call / Text &nbsp;(702) 555 - 0148</li>
        <li><svg viewBox="0 0 16 16"><path d="M2 5h12a2 2 0 0 1 2 2v7H0V7a2 2 0 0 1 2-2zM4 1h8v3H4z"/></svg>Office (902) 555 - 0172</li>
        <li><svg viewBox="0 0 16 16"><path d="M8 0a8 8 0 1 1 0 16A8 8 0 0 1 8 0zm0 2a6 6 0 1 0 0 12A6 6 0 0 0 8 2zM2 7.2h12v1.6H2z"/></svg>P.O Box 40210 Abu Dhabi, UAE</li>
      </ul>
    </div>
    <div class="services">
      <h2 class="services-title">Residential &amp; Commercial</h2>
      <ul class="services-list">
        <li>- Baby Sitting</li>
        <li>- Maid Rent</li>
        <li>- Area Rugs</li>
        <li>- Steam Carpet Care</li>
        <li>- Upholstery</li>
        <li>- Air Duct Cleaning</li>
        <li>- Tile &amp; Grout Cleaning</li>
      </ul>
    </div>
    <div class="tagline-band">
      <span class="band-dot"></span>
      <span class="tagline">Cleaner &amp; Healthier Indoor Environments</span>
      <span class="band-dot"></span>
    </div>
  </section>
</div>
</body>
</html>
```